Football field themed poster-game

I'm looking for a 22" x 29" size poster with a minimum of 300dpi, max of 300mb. File format can be jpg, gif, tiff or bmp. Would like the field portion of the poster to appear like a real grass football field. The field will need makers for each yard. I've added an addition simple clip art that shows another way for yard lines as well.The rest of the layout I would like similar, but made to look more professional. Wording should be the same as in the given draft and located in the same area or close to that area on the poster. The style is open, but should be a little minimalist in nature. Design work has to be original and cannot be taken from trademarked or copyrighted items.
Updates

Project Deadline Extended
Reason: I have 2 or 3 designs that really standout, but I would like to see just a few more.

Target Market(s)

Football fans

Font styles to use
Sans Serif

Colors

Designer to choose colors to be used in the design.

Requirements
Must have
• The design must have the same similar layout as the file I have submitted with the contest. The football field needs to be made to look like a real field with turf. boarders would be nice and a modern look.
Should not have
• hard to read fonts, changes to the major overall layout of poster.

```html
<!DOCTYPE html>
<html lang="en">
<head>
<meta charset="utf-8">
<title>Hop Huddle Field Poster</title>
<link href="https://fonts.googleapis.com/css2?family=Barlow:wght@600;700&display=swap" rel="stylesheet">
<style>
  :root {
    --backdrop: #e9e8e6;
    --score-red: #a12427;
    --gold: #c8952e;
    --white: #ffffff;
    --turf-deep: #12351c;
    --turf-border: #1b4322;
    --turf-apron: #6f9a31;
    --turf-light: #6a9c31;
    --turf-dark: #5a8b28;
  }
  html, body {
    margin: 0;
    padding: 0;
    width: 1200px;
    height: 1148px;
    overflow: hidden;
    background: var(--backdrop);
    font-family: "Barlow", Arial, sans-serif;
  }
  .poster {
    position: absolute;
    left: 190px;
    top: 34px;
    width: 820px;
    height: 1080px;
    display: flex;
    box-shadow: 0 2px 10px rgba(0,0,0,0.15);
  }
  .score-panel {
    position: relative;
    width: 190px;
    height: 100%;
    background: var(--score-red);
    color: var(--white);
  }
  .score-label {
    position: absolute;
    left: 0;
    width: 100%;
    text-align: center;
    font-weight: 700;
    font-size: 22px;
    letter-spacing: 1px;
  }
  .score-label--home { top: 44px; transform: rotate(180deg); }
  .score-label--visitors { bottom: 46px; }
  .score-circle {
    position: absolute;
    left: 30px;
    width: 124px;
    height: 124px;
    border-radius: 50%;
    background: var(--white);
    border: 3px solid var(--score-red);
    box-shadow: 0 0 0 3px var(--white);
  }
  .score-circle--home { top: 100px; }
  .score-circle--visitors { bottom: 98px; }
  .brand-plate {
    position: absolute;
    left: 24px;
    top: 330px;
    width: 136px;
    height: 420px;
    background: var(--gold);
    border-radius: 10px;
    box-shadow: 0 0 0 3px var(--score-red), 0 0 0 6px var(--white);
    display: flex;
    align-items: center;
    justify-content: center;
  }
  .brand-name {
    transform: rotate(90deg);
    white-space: nowrap;
    font-weight: 700;
    font-size: 44px;
    color: var(--score-red);
    letter-spacing: 1px;
  }
  .field {
    display: block;
    width: 630px;
    height: 1080px;
  }
  .field text {
    font-family: "Barlow", Arial, sans-serif;
    font-weight: 700;
    fill: var(--white);
  }
</style>
</head>
<body>
<div class="poster">
  <aside class="score-panel">
    <div class="score-label score-label--home">SCORE</div>
    <div class="score-circle score-circle--home"></div>
    <div class="brand-plate"><span class="brand-name">HOP HUDDLE</span></div>
    <div class="score-circle score-circle--visitors"></div>
    <div class="score-label score-label--visitors">SCORE</div>
  </aside>

  <svg class="field" viewBox="0 0 630 1080" xmlns="http://www.w3.org/2000/svg">
    <defs>
      <filter id="turf-grain" x="0" y="0" width="100%" height="100%">
        <feTurbulence type="fractalNoise" baseFrequency="0.9" numOctaves="2" result="noise"/>
        <feColorMatrix type="matrix" values="0 0 0 0 0  0 0 0 0 0.1  0 0 0 0 0  0 0 0 0.35 0" in="noise" result="grain"/>
        <feComposite in="grain" in2="SourceGraphic" operator="in" result="grainIn"/>
        <feMerge><feMergeNode in="SourceGraphic"/><feMergeNode in="grainIn"/></feMerge>
      </filter>
      <pattern id="hash-marks" x="90" y="160" width="450" height="7.6" patternUnits="userSpaceOnUse">
        <rect x="0" y="0" width="10" height="1.2" fill="#ffffff"/>
        <rect x="150" y="0" width="10" height="1.2" fill="#ffffff"/>
        <rect x="290" y="0" width="10" height="1.2" fill="#ffffff"/>
        <rect x="440" y="0" width="10" height="1.2" fill="#ffffff"/>
      </pattern>
    </defs>

    <!-- surround and apron -->
    <rect class="surround" width="630" height="1080" fill="var(--turf-deep)"/>
    <rect class="apron" x="14" y="14" width="602" height="1052" fill="var(--turf-apron)" filter="url(#turf-grain)"/>
    <rect class="sideline-border" x="60" y="50" width="510" height="980" fill="var(--turf-border)"/>

    <!-- end zones -->
    <rect class="end-zone" x="90" y="70" width="450" height="90" fill="var(--turf-border)"/>
    <rect class="end-zone" x="90" y="920" width="450" height="90" fill="var(--turf-border)"/>

    <!-- playing field stripes -->
    <g class="turf-stripes" filter="url(#turf-grain)">
      <rect x="90" y="160" width="450" height="760" fill="var(--turf-light)"/>
      <rect x="90" y="198" width="450" height="38" fill="var(--turf-dark)"/>
      <rect x="90" y="274" width="450" height="38" fill="var(--turf-dark)"/>
      <rect x="90" y="350" width="450" height="38" fill="var(--turf-dark)"/>
      <rect x="90" y="426" width="450" height="38" fill="var(--turf-dark)"/>
      <rect x="90" y="502" width="450" height="38" fill="var(--turf-dark)"/>
      <rect x="90" y="578" width="450" height="38" fill="var(--turf-dark)"/>
      <rect x="90" y="654" width="450" height="38" fill="var(--turf-dark)"/>
      <rect x="90" y="730" width="450" height="38" fill="var(--turf-dark)"/>
      <rect x="90" y="806" width="450" height="38" fill="var(--turf-dark)"/>
      <rect x="90" y="882" width="450" height="38" fill="var(--turf-dark)"/>
    </g>

    <!-- hash marks -->
    <rect class="hash-marks" x="90" y="160" width="450" height="760" fill="url(#hash-marks)"/>

    <!-- yard lines -->
    <g class="yard-lines" stroke="var(--white)" stroke-width="2">
      <line x1="90" x2="540" y1="160" y2="160"/>
      <line x1="90" x2="540" y1="198" y2="198"/>
      <line x1="90" x2="540" y1="236" y2="236"/>
      <line x1="90" x2="540" y1="274" y2="274"/>
      <line x1="90" x2="540" y1="312" y2="312"/>
      <line x1="90" x2="540" y1="350" y2="350"/>
      <line x1="90" x2="540" y1="388" y2="388"/>
      <line x1="90" x2="540" y1="426" y2="426"/>
      <line x1="90" x2="540" y1="464" y2="464"/>
      <line x1="90" x2="540" y1="502" y2="502"/>
      <line x1="90" x2="540" y1="540" y2="540"/>
      <line x1="90" x2="540" y1="578" y2="578"/>
      <line x1="90" x2="540" y1="616" y2="616"/>
      <line x1="90" x2="540" y1="654" y2="654"/>
      <line x1="90" x2="540" y1="692" y2="692"/>
      <line x1="90" x2="540" y1="730" y2="730"/>
      <line x1="90" x2="540" y1="768" y2="768"/>
      <line x1="90" x2="540" y1="806" y2="806"/>
      <line x1="90" x2="540" y1="844" y2="844"/>
      <line x1="90" x2="540" y1="882" y2="882"/>
      <line x1="90" x2="540" y1="920" y2="920"/>
    </g>

    <!-- boundary -->
    <rect class="boundary" x="90" y="70" width="450" height="940" fill="none" stroke="var(--white)" stroke-width="3"/>

    <!-- team area bands between the 30s -->
    <rect class="team-band" x="68" y="388" width="22" height="304" fill="var(--white)"/>
    <rect class="team-band-gold" x="46" y="388" width="22" height="304" fill="var(--gold)"/>
    <rect class="team-band" x="540" y="388" width="22" height="304" fill="var(--white)"/>
    <rect class="team-band-gold" x="562" y="388" width="22" height="304" fill="var(--gold)"/>

    <!-- yard numbers, left side -->
    <g class="yard-numbers" font-size="22" text-anchor="middle">
      <text transform="translate(140 236) rotate(90)" dy="7">10</text>
      <text transform="translate(140 312) rotate(90)" dy="7">20</text>
      <text transform="translate(140 388) rotate(90)" dy="7">30</text>
      <text transform="translate(140 464) rotate(90)" dy="7">40</text>
      <text transform="translate(140 540) rotate(90)" dy="7">50</text>
      <text transform="translate(140 616) rotate(90)" dy="7">40</text>
      <text transform="translate(140 692) rotate(90)" dy="7">30</text>
      <text transform="translate(140 768) rotate(90)" dy="7">20</text>
      <text transform="translate(140 844) rotate(90)" dy="7">10</text>
    </g>
    <!-- yard numbers, right side -->
    <g class="yard-numbers" font-size="22" text-anchor="middle">
      <text transform="translate(490 236) rotate(-90)" dy="7">10</text>
      <text transform="translate(490 312) rotate(-90)" dy="7">20</text>
      <text transform="translate(490 388) rotate(-90)" dy="7">30</text>
      <text transform="translate(490 464) rotate(-90)" dy="7">40</text>
      <text transform="translate(490 540) rotate(-90)" dy="7">50</text>
      <text transform="translate(490 616) rotate(-90)" dy="7">40</text>
      <text transform="translate(490 692) rotate(-90)" dy="7">30</text>
      <text transform="translate(490 768) rotate(-90)" dy="7">20</text>
      <text transform="translate(490 844) rotate(-90)" dy="7">10</text>
    </g>

    <!-- midfield name -->
    <text class="midfield-name" transform="translate(315 540) rotate(90)" font-size="30" text-anchor="middle" dy="10">HOP HUDDLE</text>

    <!-- field name along sidelines -->
    <g class="field-name" font-size="11" letter-spacing="1.5" text-anchor="middle">
      <text transform="translate(76 265) rotate(90)" dy="4">HOP HUDDLE FIELD</text>
      <text transform="translate(76 815) rotate(90)" dy="4">HOP HUDDLE FIELD</text>
      <text transform="translate(554 265) rotate(90)" dy="4">HOP HUDDLE FIELD</text>
      <text transform="translate(554 815) rotate(90)" dy="4">HOP HUDDLE FIELD</text>
    </g>

    <!-- end zone names -->
    <text class="end-zone-name" transform="translate(315 115) rotate(180)" font-size="34" letter-spacing="3" text-anchor="middle" dy="12">HOME</text>
    <text class="end-zone-name" x="315" y="965" font-size="34" letter-spacing="3" text-anchor="middle" dy="12">VISITORS</text>
  </svg>
</div>
</body>
</html>
```